I have just launched a labour hire company and lookingfor a fresh vibrant website design

I need a landing page, a description of our services and capability, as well as an enquiries link, and register candidates link. My company is called Halvora recruitment and we supply labourers, excavator operators, and machine operators to the Civil and railway industries. I would like to stick to our logo theme and colours of Bright green, although I want a brighter green please than what I have. I have attached Images I like as well plaese. I do need a much bigger website eventually.

```html
<!DOCTYPE html>
<html lang="en">
<head>
<meta charset="utf-8">
<title>Halvora Recruitment – NSW Civil & Rail Labour Specialists</title>
<link href="https://fonts.googleapis.com/css2?family=Poppins:wght@400;500;600;700&display=swap" rel="stylesheet">
<style>
:root{
  --green:#17a834;
  --green-dark:#0f8a28;
  --ink:#1c1c1c;
  --text:#3a3a3a;
  --muted:#555;
  --line:#e4e4e4;
  --foot:#ececec;
  --white:#fff;
}
*{box-sizing:border-box;margin:0;padding:0}
html,body{width:1200px;height:4648px;overflow:hidden}
body{font-family:'Poppins',sans-serif;color:var(--text);background:var(--white);position:relative}
.abs{position:absolute}
a{color:inherit;text-decoration:none}

/* header */
.brand{display:flex;flex-direction:column;line-height:1}
.brand-name{font-weight:600;font-size:30px;letter-spacing:3px;color:var(--ink)}
.brand-sub{font-size:12px;font-weight:500;letter-spacing:1px;color:var(--ink);margin-top:4px}
.nav{left:412px;top:52px;display:flex;gap:27px;font-size:17px;color:var(--ink)}
.btn-outline{border:2px solid var(--green);color:var(--green);font-weight:500;display:flex;align-items:center;justify-content:center;background:var(--white)}
.header-rule{left:0;top:124px;width:1200px;height:2px;background:var(--line)}

/* hero */
.hero{left:0;top:126px;width:1200px;height:530px;background:var(--green)}
.hero-frame{border:3px solid rgba(255,255,255,.08)}
.hero-photo{left:800px;top:126px;width:400px;height:530px;background:linear-gradient(160deg,#d9d1c4 0%,#8a6a4a 35%,#3d3b3a 70%,#e26b1f 100%);clip-path:polygon(30% 0,100% 0,100% 100%,0 100%,12% 60%,20% 25%)}
.hero-title{left:183px;top:240px;width:600px;text-align:center;color:var(--white);font-weight:600;font-size:38px;line-height:52px}
.hero-sub{left:183px;top:352px;width:600px;text-align:center;color:var(--white);font-size:18px;line-height:27px}
.btn-white{left:392px;top:432px;width:168px;height:54px;background:var(--white);color:var(--green);font-weight:600;font-size:17px;display:flex;align-items:center;justify-content:center}

/* section headings */
.heading{font-weight:700;font-size:40px;color:var(--ink);line-height:1}
.deco{display:flex;align-items:center;gap:12px;margin-top:8px}
.deco i{display:block;width:22px;height:6px;background:var(--green)}
.deco b{display:block;width:130px;height:7px;border-top:2px solid var(--green);border-bottom:2px solid var(--green)}
.deco em{display:block;width:3px;height:12px;background:var(--green)}
.center{text-align:center}
.center .deco{justify-content:center}

/* about */
.about-text{left:85px;top:843px;width:615px;font-size:17.5px;line-height:26.6px}
.about-visual{left:712px;top:735px;width:440px;height:455px;background:linear-gradient(150deg,#e3e8ee 0%,#c4cfdb 60%,#aebccb 100%)}

/* services */
.card{width:304px;background:var(--white);border:2px solid #f0f0f0;border-radius:8px;box-shadow:0 2px 6px rgba(0,0,0,.06);overflow:hidden;text-align:center}
.card.active{border:4px solid var(--green)}
.card-media{height:182px;position:relative;display:flex;align-items:flex-end;justify-content:center;padding-bottom:10px}
.card-media span{position:relative;color:var(--white);font-weight:600;font-size:17px}
.card.active .card-media{align-items:center;padding:0}
.card.active .card-media span{font-size:26px;line-height:34px}
.card-text{font-size:14px;line-height:24px;padding:14px 16px 0;height:140px;color:var(--muted)}
.card .btn-outline{width:162px;height:52px;margin:0 auto 30px;font-size:17px;font-weight:400}

/* why */
.why-item{display:flex;align-items:center}
.why-num{font-size:40px;font-weight:500;color:var(--green);width:70px}
.why-mark{width:125px;height:82px;background:var(--green);margin-right:10px}
.why-text{border-left:2px solid #bbb;padding-left:14px;font-size:15px;line-height:24px;width:300px}

/* clients */
.band{left:0;top:3256px;width:1200px;height:206px;background:var(--green)}
.portrait{left:153px;top:3191px;width:330px;height:330px;border-radius:50%;border:6px solid var(--white);background:radial-gradient(circle at 50% 45%,#c7c9d4,#5e6a9e 70%,#2a2f6a)}
.client-name{left:545px;top:3288px;color:var(--white);font-size:26px;font-weight:600}
.client-name small{font-size:17px;font-weight:400}
.client-name .stars{color:#ffe100;font-size:18px;letter-spacing:1px}
.client-quote{left:545px;top:3332px;width:420px;color:var(--white);font-size:15px;line-height:24px}
.dots{left:996px;top:3454px;display:flex;gap:8px;align-items:center}
.dots span{width:9px;height:9px;border-radius:50%;background:var(--white)}
.dots span:first-child{width:14px;height:14px;border:2px solid #333}

/* enquiry */
.enquiry{left:161px;top:3745px;width:890px;height:560px;background:var(--green)}
.contact-line{color:var(--white);font-size:18px;line-height:27px;text-align:center}
.field-label{color:var(--white);font-size:18px}
.field-line{height:2px;background:rgba(255,255,255,.8);width:440px}
.btn-ghost{border:2px solid var(--white);color:var(--white);font-weight:500;font-size:18px;display:flex;align-items:center;justify-content:center}

/* footer */
.footer{left:0;top:4375px;width:1200px;height:273px;background:var(--foot)}
.foot-title{font-weight:600;font-size:17px;color:var(--ink)}
.foot-list{list-style:none;font-size:15px;line-height:24px;margin-top:10px}
.foot-list li::before{content:"";display:inline-block;width:10px;height:7px;border-top:2px solid var(--green);border-bottom:2px solid var(--green);margin-right:8px}
.copyright{left:0;top:4614px;width:1200px;text-align:center;color:var(--green);font-size:15px}
</style>
</head>
<body>

<header>
  <a class="abs brand" style="left:63px;top:40px" href="#">
    <span class="brand-name">HALVORA</span>
    <span class="brand-sub">RECRUITMENT PTY LTD</span>
  </a>
  <nav class="abs nav"><a>Home</a><a>About us</a><a>Services</a><a>Enquiries</a><a>Contact</a></nav>
  <a class="abs btn-outline" style="left:918px;top:34px;width:234px;height:56px;font-size:17px">Register Candidates</a>
  <div class="abs header-rule"></div>
</header>

<section>
  <div class="abs hero"></div>
  <div class="abs hero-frame" style="left:66px;top:126px;width:150px;height:530px"></div>
  <div class="abs hero-frame" style="left:266px;top:130px;width:500px;height:82px"></div>
  <div class="abs hero-frame" style="left:266px;top:565px;width:500px;height:82px"></div>
  <div class="abs hero-photo" role="img" aria-label="Civil worker in hard hat carrying a concrete pipe on his shoulder"></div>
  <h1 class="abs hero-title">NSW CIVIL &amp;<br>RAIL LABOUR SPECIALISTS</h1>
  <p class="abs hero-sub">Halvora Recruitment is a NSW labour hire agency<br>specialising in the civil sector</p>
  <a class="abs btn-white">CONTACT</a>
</section>

<section>
  <div class="abs" style="left:85px;top:755px">
    <h2 class="heading">ABOUT US</h2>
    <div class="deco"><i></i><i></i><b></b><em></em></div>
  </div>
  <p class="abs about-text">Halvora Recruitment is a NSW labour hire agency specialising in the civil sector. With a strong track record of providing skilled and reliable workers to the civil and rail construction industry, we have established ourselves as a trusted partner for companies seeking efficient and cost-effective staffing solutions. Our team of experienced professionals is dedicated to meeting the specific needs of our clients, ensuring seamless project execution and successful outcomes..</p>
  <a class="abs btn-outline" style="left:85px;top:1087px;width:163px;height:53px;font-size:17px;font-weight:400">Read More</a>
  <div class="abs about-visual" role="img" aria-label="Map of Australia with the national flag on a pole"></div>
</section>

<section>
  <div class="abs" style="left:88px;top:1285px">
    <h2 class="heading">SERVICES</h2>
    <div class="deco"><i></i><i></i><b></b><em></em></div>
  </div>

  <article class="abs card active" style="left:110px;top:1413px;height:448px">
    <div class="card-media" role="img" aria-label="Heavy mining haul truck" style="background:linear-gradient(#6b6558,#2d2a25)"><span>Rigorous<br>Selection Process</span></div>
    <p class="card-text">Halvora Recruitment employs a meticulous selection process to identify and choose the most qualified and experienced civil labourers and operators.</p>
    <a class="btn-outline">View More</a>
  </article>

  <article class="abs card" style="left:458px;top:1417px;height:440px">
    <div class="card-media" role="img" aria-label="Yellow excavator on a work site" style="background:linear-gradient(#9fb0b8,#6d6a55 60%,#2b2b2b)"><span>Compliance Verification</span></div>
    <p class="card-text">The agency places a strong emphasis on compliance with industry regulations and standards. They verify that all candidates possess the necessary licenses,</p>
    <a class="btn-outline">View More</a>
  </article>

  <article class="abs card" style="left:802px;top:1417px;height:440px">
    <div class="card-media" role="img" aria-label="Railway tracks in a rail yard" style="background:linear-gradient(#b8b2a2,#7a6b57 60%,#2b2b2b)"><span>Reference Checking</span></div>
    <p class="card-text">By contacting previous employers or supervisors, the agency gains insights into a candidate's skill set, work ethic, and overall suitability for the</p>
    <a class="btn-outline">View More</a>
  </article>

  <article class="abs card" style="left:295px;top:1940px;height:420px">
    <div class="card-media" role="img" aria-label="Concrete being levelled by hand" style="background:linear-gradient(#c9a887,#6f6e6a 60%,#2b2b2b)"><span>Skill Assessment</span></div>
    <p class="card-text" style="height:124px">The agency assesses the technical competencies and skill levels of each candidate during the selection processs.</p>
    <a class="btn-outline">View More</a>
  </article>

  <article class="abs card" style="left:640px;top:1940px;height:420px">
    <div class="card-media" role="img" aria-label="Two workers in white hard hats on site" style="background:linear-gradient(#dfe3ea,#5a6d8d 55%,#7a1020)"><span>Industry Experience</span></div>
    <p class="card-text" style="height:124px">Halvora Recruitment has an extensive network and deep knowledge of the civil and railway industries in NSW.</p>
    <a class="btn-outline">View More</a>
  </article>
</section>

<section>
  <div class="abs center" style="left:0;top:2462px;width:1236px">
    <h2 class="heading">WHY CHOOSE US</h2>
    <div class="deco"><i></i><i></i><b style="width:210px"></b><em></em></div>
  </div>
  <div class="abs" style="left:605px;top:2580px;width:1px;height:360px;background:#ccc"></div>

  <div class="abs why-item" style="left:82px;top:2604px"><span class="why-num">01</span><span class="why-mark"></span><p class="why-text">Lorem ipsum dolor sit amet, consectetur adipiscing elit, sed do eiusmod tempor incididunt ut labore et dolore magna aliqua.</p></div>
  <div class="abs why-item" style="left:642px;top:2604px"><span class="why-num">02</span><span class="why-mark"></span><p class="why-text">Lorem ipsum dolor sit amet, consectetur adipiscing elit, sed do eiusmod tempor incididunt ut labore et dolore magna aliqua.</p></div>
  <div class="abs why-item" style="left:78px;top:2778px"><span class="why-num">03</span><span class="why-mark"></span><p class="why-text">Lorem ipsum dolor sit amet, consectetur adipiscing elit, sed do eiusmod tempor incididunt ut labore et dolore magna aliqua.</p></div>
  <div class="abs why-item" style="left:636px;top:2778px"><span class="why-num">04</span><span class="why-mark"></span><p class="why-text">Lorem ipsum dolor sit amet, consectetur adipiscing elit, sed do eiusmod tempor incididunt ut labore et dolore magna aliqua.</p></div>
</section>

<section>
  <div class="abs center" style="left:0;top:3053px;width:1220px">
    <h2 class="heading">OUR HAPPY CLIENTS</h2>
    <div class="deco"><i style="width:44px"></i><i style="width:44px"></i><b style="width:260px"></b><em></em></div>
  </div>
  <div class="abs band"></div>
  <div class="abs portrait" role="img" aria-label="Portrait photo of the client"></div>
  <p class="abs client-name">Marcus Hale <small>(CEO ,Corvan)</small> <span class="stars">★★★★★</span></p>
  <p class="abs client-quote">Lorem ipsum dolor sit amet, consectetur adipiscing elit, sed do eiusmod tempor incididunt ut labore et dolore magna aliqua. Quis ipsum suspendisse ultrices graccumsan lacus vel facilisis.</p>
  <svg class="abs" style="left:996px;top:3335px" width="70" height="36" viewBox="0 0 70 36" aria-hidden="true">
    <polyline points="24,4 10,18 24,32" fill="none" stroke="rgba(255,255,255,.55)" stroke-width="7"/>
    <polyline points="44,4 58,18 44,32" fill="none" stroke="#fff" stroke-width="7"/>
  </svg>
  <div class="abs dots"><span></span><span></span><span></span><span></span><span></span><span></span><span></span></div>
</section>

<section>
  <div class="abs center" style="left:0;top:3613px;width:1220px">
    <h2 class="heading">ENQUIRES</h2>
    <div class="deco"><i></i><i></i><b></b><em></em></div>
  </div>
  <div class="abs enquiry"></div>

  <svg class="abs" style="left:252px;top:3860px" width="70" height="80" viewBox="0 0 24 24" aria-hidden="true">
    <path fill="#fff" d="M6.6 2.5l3 3.6-1.9 2.4c1.2 2.7 3.2 4.8 5.9 6l2.4-1.9 3.6 3-2.2 3.4C10.2 19 4.8 13.6 3.4 4.7z"/>
  </svg>
  <p class="abs contact-line" style="left:161px;top:3953px;width:265px">0400-555-182</p>

  <svg class="abs" style="left:268px;top:4040px" width="54" height="72" viewBox="0 0 24 32" aria-hidden="true">
    <path fill="#fff" d="M12 0C5.4 0 0 5.4 0 12c0 8.5 12 20 12 20s12-11.5 12-20C24 5.4 18.6 0 12 0zm0 17a5 5 0 110-10 5 5 0 010 10z"/>
  </svg>
  <p class="abs contact-line" style="left:161px;top:4140px;width:285px">Sydney ,12 Larkin Street<br>3rd Floor<br>Australia</p>

  <svg class="abs" style="left:439px;top:3805px" width="18" height="480" aria-hidden="true">
    <rect x="2" y="0" width="13" height="60" fill="#fff"/>
    <rect x="2" y="78" width="13" height="52" fill="#fff"/>
    <rect x="3" y="148" width="3" height="310" fill="#fff"/>
    <rect x="11" y="148" width="3" height="310" fill="#fff"/>
    <rect x="2" y="465" width="13" height="15" fill="#fff"/>
  </svg>

  <h3 class="abs" style="left:532px;top:3792px;color:#fff;font-size:42px;font-weight:600">Get In Touch</h3>
  <span class="abs" style="left:830px;top:3818px;width:44px;height:28px;border-top:4px solid #fff;border-bottom:4px solid #fff"></span>

  <label class="abs field-label" style="left:538px;top:3890px">Name</label>
  <div class="abs field-line" style="left:536px;top:3932px"></div>
  <label class="abs field-label" style="left:536px;top:3967px">E-mail</label>
  <div class="abs field-line" style="left:536px;top:4010px"></div>
  <label class="abs field-label" style="left:536px;top:4044px">Meesage</label>
  <div class="abs field-line" style="left:536px;top:4155px"></div>
  <a class="abs btn-ghost" style="left:803px;top:4205px;width:169px;height:53px">Enquire</a>
</section>

<footer>
  <div class="abs footer"></div>
  <div class="abs brand" style="left:78px;top:4455px">
    <span class="brand-name">HALVORA</span>
    <span class="brand-sub">RECRUITMENT PTY LTD</span>
  </div>
  <div class="abs" style="left:88px;top:4552px;width:98px;height:1px;background:var(--green)"></div>
  <div class="abs" style="left:202px;top:4543px;display:flex;gap:10px">
    <span style="width:16px;height:16px;border-radius:50%;background:var(--green)"></span>
    <span style="width:16px;height:16px;border-radius:50%;background:var(--green)"></span>
    <span style="width:16px;height:16px;border-radius:50%;background:var(--green)"></span>
  </div>
  <div class="abs" style="left:286px;top:4552px;width:100px;height:1px;background:var(--green)"></div>

  <div class="abs" style="left:445px;top:4435px">
    <p class="foot-title">Quick Links</p>
    <div class="deco" style="margin-top:2px;gap:5px"><i style="width:12px;height:4px"></i><i style="width:12px;height:4px"></i><b style="width:60px;height:5px;border-width:1px"></b></div>
    <ul class="foot-list" style="margin-top:4px"><li>Home</li><li>About Us</li><li>Enquires</li><li>Contact</li></ul>
  </div>
  <div class="abs" style="left:625px;top:4435px">
    <p class="foot-title">Legal</p>
    <div class="deco" style="margin-top:2px;gap:5px"><i style="width:12px;height:4px"></i><i style="width:12px;height:4px"></i><b style="width:90px;height:5px;border-width:1px"></b></div>
    <ul class="foot-list" style="margin-top:4px"><li>Terms of Use</li><li>Terms &amp; Condition</li><li>Privacy Policy</li><li>Cookie Policy</li></ul>
  </div>
  <div class="abs" style="left:838px;top:4435px;width:290px">
    <p class="foot-title">News Letter</p>
    <div class="deco" style="margin-top:2px;gap:5px"><i style="width:12px;height:4px"></i><i style="width:12px;height:4px"></i><b style="width:60px;height:5px;border-width:1px"></b></div>
    <p style="font-size:15px;line-height:24px;margin-top:8px">Join Our Newsletter to stay upto date with our latest updates</p>
    <div style="display:flex;margin-top:14px">
      <span style="width:202px;height:40px;background:#fff;color:#bbb;font-size:14px;padding:9px 10px">Enter your E-mail</span>
      <span style="width:82px;height:40px;background:var(--green);color:#fff;font-weight:600;font-size:15px;display:flex;align-items:center;justify-content:center">Submit</span>
    </div>
  </div>
  <p class="abs copyright">Copyrights @ lorem 2023 all rights reserved</p>
</footer>

</body>
</html>
```